Riverbend Trusted Home Care-Flyer for Patients

Our Home Health Care Agency, Riverbend Trusted Home Care, is seeking a flyer to advertise our services. We would like our flyer to convey professionalism, classiness and sophistication. We want our agency to come across as one that is well-established and recognized as being first-rate within the field.

We also want to appear original; we want to stand out.

Our theme colors, blue and green, from our logo should be incorporated into the flyer's design (refer below).

The top of the page should say (in a clear, bold font)-Seeking Care for your Loved One?

Our Logo, followed by our slogan, "Lean On Those Nearby", should be in the center. (This should make it appear as if our agency is the obvious solution to the consumer's quest in finding suitable care for their family member). This should be in a big font.
Below that, our agency's services should be listed in a very noticeable font...yet smaller than what's written above that.
The text should read:
Our Services Include:
*Experienced Certified Home Health Aides/ Live In Home Health Aides/Companions
*Nursing Services
*Alzheimer’s and Dementia Care
*Respite Care
*Postoperative Care
*Post Rehabilitation Care
*Running Errands
*Light Housekeeping
*Assistance with Bathing, Feeding and Grooming
*Meal Preparation
*Laundry and Linen Washing
*Mail and Bill Organization
*Medication Management
*Accompanying to Doctor’s Appointments
*And much more!
Below that, in a smaller, yet noticeable font:
As seasoned professionals, we know how to help our clients navigate and fulfill their various health care needs. Those nearby are here to help you get the attention that you merit.
Call Riverbend Trusted Home Care today to learn more about our first-rate services!
Below that, in a larger font, our phone number, website, our e-mail address.
*Out contact information will be provided to the project’s winner*.

*Pictures of Caregivers helping elderly patient should be included in the advertisement as well. *

We provided advertisements of other Home Health Care Agencies attached below to use as a reference. Once again, while we are aiming for a similar idea; however, our goal is to stand out as the community's premiere home health care agency, the one that they want to choose. We want to be original as well!

Size: Standard Computer Paper Size. 8.5” x 11”.

Feel free to utilize your creative, designer flair!
We look forward to seeing the results!
Good luck!

Industry/Entity Type

Home Health Care

Font styles to use
Sans Serif

Requirements
Must have
• Refer above.
Nice to have
• Refer to attachment below to see how other home health care agencies advertise. While we are aiming for a similar idea, we would like to incorporate our logo, slogan and colors to make this flyer more unique and stand out. We would like to appear original.

```html
<!DOCTYPE html>
<html lang="en">
<head>
<meta charset="utf-8">
<title>Riverbend Trusted Home Care – Patient Flyer</title>
<link rel="stylesheet" href="https://fonts.googleapis.com/css2?family=Montserrat:wght@700;800&family=Oswald:wght@600;700&family=Questrial&display=swap">
<style>
  :root {
    --brand-blue: #0b54a2;
    --ink-blue: #0c4e9b;
    --brand-green: #8cc63f;
    --heart-green: #5ba42f;
    --paper: #ffffff;
    --photo-light: #e9e5df;
    --photo-mid: #b9c6d4;
    --photo-warm: #cdbba4;
  }
  * { box-sizing: border-box; margin: 0; padding: 0; }
  html, body { width: 908px; height: 1200px; overflow: hidden; background: var(--paper); }
  .flyer { position: relative; width: 908px; height: 1200px; overflow: hidden; background: var(--brand-blue); }
  .backdrop { position: absolute; inset: 0; }

  .photo {
    position: absolute; border-radius: 50%;
    border: 6px solid var(--paper);
    box-shadow: 0 4px 10px rgba(0,0,0,.25);
  }
  .photo--hero { left: -174px; top: -115px; width: 730px; height: 730px; border-width: 8px;
    background: radial-gradient(circle at 60% 55%, var(--photo-mid), var(--photo-light) 45%, var(--photo-warm)); }
  .photo--visit { left: 292px; top: 424px; width: 194px; height: 194px;
    background: linear-gradient(135deg, var(--photo-warm), #f0e6da 55%, #9aa3ad); }
  .photo--garden { left: 511px; top: 522px; width: 166px; height: 166px;
    background: linear-gradient(135deg, #6e9a5c, #dfe7ea 50%, #2d5fa8); }
  .photo--support { left: 708px; top: 642px; width: 150px; height: 150px;
    background: linear-gradient(135deg, var(--photo-light), var(--photo-mid) 60%, #d8cdbf); }

  .services { position: absolute; left: 589px; top: 40px; width: 300px; color: var(--paper); }
  .services__title { font-family: "Montserrat", sans-serif; font-weight: 800; font-size: 25px;
    line-height: 30px; color: var(--brand-green); margin-bottom: 4px; }
  .services__list { list-style: none; font-family: "Questrial", sans-serif; font-size: 15.4px; line-height: 22.5px; }
  .services__list li { position: relative; padding-left: 15px; }
  .services__list li::before { content: ""; position: absolute; left: 0; top: 6px; width: 10px; height: 10px;
    border: 1px solid var(--brand-green); border-radius: 50%; }
  .services__list li::after { content: ""; position: absolute; left: 3px; top: 8px; width: 5px; height: 3px;
    border-left: 1.5px solid var(--brand-green); border-bottom: 1.5px solid var(--brand-green); transform: rotate(-45deg); }

  .headline { position: absolute; left: 0; top: 0; width: 520px; height: 960px; }
  .headline__text { font-family: "Oswald", sans-serif; font-weight: 700; fill: var(--ink-blue); text-transform: uppercase; }
  .heart { position: absolute; left: 371px; top: 771px; width: 104px; height: 90px; }
  .heart__text { position: absolute; left: 371px; top: 782px; width: 104px; text-align: center;
    font-family: "Oswald", sans-serif; font-weight: 700; font-size: 20px; line-height: 27px; color: var(--paper); }

  .brand { position: absolute; left: 99px; top: 966px; width: 300px; text-align: center; color: var(--ink-blue); }
  .brand__mark { display: block; width: 100px; height: 100px; margin: 0 auto 12px; border-radius: 50%; background: var(--ink-blue); }
  .brand__name { font-family: "Montserrat", sans-serif; font-weight: 700; font-size: 19px; line-height: 22px; text-transform: uppercase; }
  .brand__slogan { margin-top: 6px; font-family: "Questrial", sans-serif; font-size: 11px; letter-spacing: 3.2px; text-transform: uppercase; }

  .pitch { position: absolute; left: 549px; top: 832px; width: 320px; font-family: "Questrial", sans-serif;
    font-size: 17.4px; line-height: 23px; color: var(--paper); }
  .cta { position: absolute; left: 549px; top: 1000px; width: 320px; font-family: "Oswald", sans-serif; font-weight: 600;
    font-size: 18px; line-height: 24px; color: var(--brand-green); text-transform: uppercase; }

  .contact { position: absolute; left: 466px; top: 1100px; width: 440px; color: var(--ink-blue); }
  .contact__phone { display: flex; align-items: center; gap: 8px; font-family: "Montserrat", sans-serif;
    font-weight: 700; font-size: 33px; line-height: 42px; }
  .contact__phone-icon { width: 38px; height: 38px; flex: none; }
  .contact__row { display: flex; gap: 26px; margin-top: 4px; margin-left: 4px; font-family: "Questrial", sans-serif; font-size: 15.5px; line-height: 22px; }
  .contact__item { display: flex; align-items: center; gap: 9px; }
  .contact__icon { width: 15px; height: 15px; flex: none; }
</style>
</head>
<body>
<main class="flyer">
  <svg class="backdrop" width="908" height="1200" viewBox="0 0 908 1200" aria-hidden="true">
    <path fill="var(--paper)" d="M0,0 H470 C540,60 565,170 560,260 C555,370 500,450 488,540 C480,620 500,680 517,730 C530,780 535,860 528,900 C520,970 500,1040 469,1091 L388,1200 H0 Z"/>
    <path fill="var(--brand-green)" d="M469,1091 H908 V1200 H388 Z"/>
  </svg>

  <div class="photo photo--hero" role="img" aria-label="Photo: young caregiver resting a hand on the shoulder of a smiling elderly man in a wheelchair"></div>
  <div class="photo photo--visit" role="img" aria-label="Photo: nurse holding the hand of a cheerful elderly woman"></div>
  <div class="photo photo--garden" role="img" aria-label="Photo: nurse in blue scrubs helping an elderly woman outdoors"></div>
  <div class="photo photo--support" role="img" aria-label="Photo: caregiver supporting an elderly man seated in a wheelchair"></div>

  <section class="services">
    <h2 class="services__title">OUR SERVICES<br>INCLUDE:</h2>
    <ul class="services__list">
      <li>Experienced Certified Home<br>Health Aides/ Live In Home<br>Health Aides/Companions</li>
      <li>Nursing Services</li>
      <li>Alzheimer’s and Dementia Care</li>
      <li>Respite Care</li>
      <li>Postoperative Care</li>
      <li>Post Rehabilitation Care</li>
      <li>Running Errands</li>
      <li>Light Housekeeping</li>
      <li>Assistance with Bathing,<br>Feeding and Grooming</li>
      <li>Meal Preparation</li>
      <li>Laundry and Linen Washing</li>
      <li>Mail and Bill Organization</li>
      <li>Medication Management</li>
      <li>Accompanying to Doctor’s<br>Appointments</li>
    </ul>
  </section>

  <svg class="headline" viewBox="0 0 520 960" role="heading" aria-level="1" aria-label="Seeking care for your loved one?">
    <text class="headline__text" x="52" y="752" font-size="111" textLength="420" lengthAdjust="spacingAndGlyphs">SEEKING</text>
    <text class="headline__text" x="47" y="870" font-size="135" textLength="319" lengthAdjust="spacingAndGlyphs">CARE</text>
    <text class="headline__text" x="50" y="947" font-size="78" textLength="429" lengthAdjust="spacingAndGlyphs">LOVED ONE?</text>
  </svg>
  <svg class="heart" viewBox="0 0 106 92" preserveAspectRatio="none" aria-hidden="true">
    <path fill="var(--heart-green)" d="M53,92 L9,46 C-6,30 2,2 26,1 C40,0 49,9 53,17 C57,9 66,0 80,1 C104,2 112,30 97,46 Z"/>
  </svg>
  <div class="heart__text">FOR<br>YOUR</div>

  <div class="brand">
    <span class="brand__mark" aria-hidden="true"></span>
    <p class="brand__name">Riverbend Trusted<br>Home Care</p>
    <p class="brand__slogan">Lean On Those Nearby</p>
  </div>

  <p class="pitch">As seasoned professionals, we know how to help our clients navigate and fulfill their various health care needs. Those nearby are here to help you get the attention that you merit.</p>
  <p class="cta">Call Riverbend Trusted Home Care today to learn more about our first-rate services!</p>

  <div class="contact">
    <p class="contact__phone">
      <svg class="contact__phone-icon" viewBox="0 0 38 38" aria-hidden="true">
        <circle cx="19" cy="19" r="19" fill="var(--ink-blue)"/>
        <path fill="var(--paper)" d="M13,10 l4,0 l2,6 l-3,2 c1.5,3 3,4.5 6,6 l2,-3 l6,2 l0,4 c0,1.5 -1,2 -2.5,2 C18,28.5 9.5,20 9.5,12.5 C9.5,11 11.5,10 13,10 Z"/>
      </svg>
      (555) 214-3380
    </p>
    <div class="contact__row">
      <span class="contact__item">
        <svg class="contact__icon" viewBox="0 0 15 15" aria-hidden="true"><rect width="15" height="15" rx="3" fill="var(--paper)"/><rect x="3" y="4.5" width="9" height="6" fill="var(--ink-blue)"/><path d="M3,4.5 L7.5,8 L12,4.5" stroke="var(--paper)" stroke-width="1" fill="none"/></svg>
        hi@riverbendcare.com
      </span>
      <span class="contact__item">
        <svg class="contact__icon" viewBox="0 0 15 15" aria-hidden="true"><rect width="15" height="15" rx="3" fill="var(--paper)"/><path d="M6,9 L9,6 M5,7.5 l-1,1 a1.8,1.8 0 0 0 2.5,2.5 l1,-1 M10,7.5 l1,-1 a1.8,1.8 0 0 0 -2.5,-2.5 l-1,1" stroke="var(--ink-blue)" stroke-width="1.2" fill="none" stroke-linecap="round"/></svg>
        www.riverbendcare.com
      </span>
    </div>
  </div>
</main>
</body>
</html>
```